feld+klang
Zielgruppe
HÖRWEGE IM FREIEN, Entwicklung von Audio-Guides für Draußen
potentielle Auftraggeber: Standortmarketing, Tourismusmarketing, Gemeinden, Kulturinstitutionen
Aufgabenstellung
Layout Briefkopf /Visitenkarte
Text:
Feld und Klang (feld+klang)
HÖRWEGE IM FREIEN
www.feld-und-klang-beispiel.de
Visitenkarte Rückseite: Landschaften hörbar machen...
Das PDF zeigt einen ersten Versuch meinerseits, ich bin aber auch für ganz andere Vorschläge offen. Generell stelle ich mir eine schlichte Typographie vor, ohne Icons oder Ähnliches.

```html
<!DOCTYPE html>
<html lang="de">
<head>
<meta charset="utf-8">
<title>feld+klang – Geschäftsausstattung</title>
<link href="https://fonts.googleapis.com/css2?family=Exo+2:ital,wght@1,400&family=Source+Sans+3:wght@400;600;700&display=swap" rel="stylesheet">
<style>
  :root {
    --bg: #f7f7f7;
    --paper: #ffffff;
    --envelope: #f0f0f0;
    --red: #c1272d;
    --ink: #3a3a3a;
    --grey: #7a7a7a;
    --text: #4a4a4a;
    --line: #9a9a9a;
    --shadow: 3px 4px 5px rgba(0,0,0,0.35);
  }
  * { margin: 0; padding: 0; box-sizing: border-box; }
  html, body { width: 1200px; height: 1000px; overflow: hidden; background: var(--bg); }
  body { position: relative; font-family: "Source Sans 3", sans-serif; color: var(--text); }

  .sheet { position: absolute; background: var(--paper); box-shadow: var(--shadow); }

  .brand { position: absolute; text-align: right; line-height: 1; white-space: nowrap; }
  .brand-name { display: block; color: var(--ink); font-weight: 600; font-size: 24px; letter-spacing: 0.3px; }
  .brand-tag { display: block; color: var(--grey); font-weight: 400; font-size: 11px; letter-spacing: 2.6px; margin-top: 4px; }

  .address { position: absolute; font-size: 8px; line-height: 10px; text-align: right; white-space: nowrap; }

  /* Briefbogen */
  .letterhead { left: 29px; top: 111px; width: 533px; height: 753px; }
  .letterhead .brand { right: 28px; top: 33px; }
  .letterhead .sender { right: 28px; top: 80px; }
  .letterhead .contact { right: 28px; top: 115px; }
  .fold-mark { position: absolute; left: 0; width: 20px; height: 1px; background: var(--line); }
  .fold-mark.upper { top: 263px; }
  .fold-mark.lower { top: 501px; }
  .legal { position: absolute; left: 0; width: 533px; text-align: center; font-size: 7px; color: var(--grey); }
  .legal.register { top: 711px; }
  .legal.bank { top: 727px; }
  .legal .gap { display: inline-block; width: 12px; }
  .red-bar { position: absolute; background: var(--red); height: 10px; width: 153px; }
  .letterhead .red-bar { left: 189px; bottom: 1px; }

  /* Umschlag */
  .envelope { position: absolute; left: 598px; top: 38px; width: 562px; height: 390px; }
  .envelope-shape { position: absolute; left: 0; top: 0; filter: drop-shadow(3px 4px 3px rgba(0,0,0,0.3)); }
  .flap-name { position: absolute; left: 0; width: 560px; top: 44px; text-align: center; transform: rotate(180deg);
    color: var(--grey); font-weight: 600; font-size: 20px; letter-spacing: 0.3px; line-height: 1; }
  .envelope .sender { right: 410px; top: 153px; }
  .envelope .brand { right: 44px; top: 293px; }
  .envelope .red-bar { left: 204px; top: 378px; }

  /* Visitenkarten */
  .card { width: 295px; height: 176px; }
  .card-front { left: 758px; top: 469px; }
  .card-front .brand { left: 19px; top: 20px; text-align: left; }
  .card-front .brand-tag { font-size: 12px; letter-spacing: 2.8px; margin-top: 5px; }
  .card-front .address { text-align: left; top: 120px; }
  .card-front .col-left { left: 19px; }
  .card-front .col-right { left: 145px; top: 130px; }
  .web-tab { position: absolute; right: 0; top: 24px; width: 20px; height: 128px; background: var(--red);
    border-radius: 8px 0 0 8px; }
  .web-tab span { position: absolute; left: 50%; top: 50%; transform: translate(-50%, -50%) rotate(-90deg);
    white-space: nowrap; color: #fff; font-size: 7px; }

  .card-back { left: 758px; top: 688px; }
  .claim { position: absolute; font-family: "Exo 2", sans-serif; font-style: italic; font-size: 19px; color: #1a1a1a; line-height: 1; white-space: nowrap; }
  .claim.first { left: 32px; top: 63px; }
  .claim.second { left: 71px; top: 87px; }
</style>
</head>
<body>

<section class="sheet letterhead" aria-label="Briefbogen">
  <div class="brand"><span class="brand-name">feld+klang</span><span class="brand-tag">HÖRWEGE IM FREIEN</span></div>
  <p class="address sender">Mira Albers,<br>Am Lindenhang 7,<br>79100 Musterstadt-Tal</p>
  <p class="address contact">Tel. 49 170 0000123<br>e-mail: albers@feldklang.example</p>
  <span class="fold-mark upper"></span>
  <span class="fold-mark lower"></span>
  <p class="legal register">Zugelassen beim Amtsgericht und Landgericht Musterstadt Bankverbindung: SPK-BT</p>
  <p class="legal bank">IBAN: DE00 1234 5678 0000 123 456 7<span class="gap"></span>BIC: BSPLDE00XXX</p>
  <span class="red-bar"></span>
</section>

<section class="envelope" aria-label="Briefumschlag">
  <svg class="envelope-shape" width="562" height="392" viewBox="0 0 562 392" aria-hidden="true">
    <path d="M0 99 L0 388 L560 388 L560 99 L560 80 Q558 52 530 48 L290 0 Q280 -2 270 0 L30 48 Q2 52 0 80 Z" fill="#f0f0f0"/>
    <line x1="0" y1="99.5" x2="560" y2="99.5" stroke="#d8d8d8" stroke-width="1"/>
  </svg>
  <div class="flap-name">feld+klang</div>
  <p class="address sender">Mira Albers,<br>Am Lindenhang 7,<br>79100 Musterstadt-Tal</p>
  <div class="brand"><span class="brand-name">feld+klang</span><span class="brand-tag">HÖRWEGE IM FREIEN</span></div>
  <span class="red-bar"></span>
</section>

<section class="sheet card card-front" aria-label="Visitenkarte Vorderseite">
  <div class="brand"><span class="brand-name">feld+klang</span><span class="brand-tag">HÖRWEGE IM FREIEN</span></div>
  <p class="address col-left">Mira Albers,<br>Am Lindenhang 7,<br>79100 Musterstadt-Tal</p>
  <p class="address col-right">Tel. 49 170 0000123<br>e-mail: albers@feldklang.example</p>
  <div class="web-tab"><span>www.feld-und-klang-beispiel.de</span></div>
</section>

<section class="sheet card card-back" aria-label="Visitenkarte Rückseite">
  <p class="claim first">Landschaften</p>
  <p class="claim second">hörbar machen...</p>
</section>

</body>
</html>
```